Monthly Mailed Newsletter/Magazine for Medical Spa

Every month we send out a mailed newsletter/magazine to our visitors from the previous month. We made a sample newsletter/magazine as a guideline of what we are looking for. We need a designer to make a simple and clean design layout.

- Attached is our sample design that has all the content we want to use.
- Newsletter/magazine is 8 pages total.
- Size of each page is 8.5 inches in width by 11 inches in height.
- Content and images can be located here: https://files.vornacloud.net/shared/8kqTRw3ZpLmX2vNcA7yHd5EbJ0sUgFo4e?view=open

The following will give you an idea of our brand presentation.
Our website is: www.GlowDermaClinic.com
Our Instagram; @glowdermaclinic
Our Facebook: www.socialtreo.com/glowdermaclinic

Target Market(s)

Women 25 - 45

Industry/Entity Type

Beauty

Font styles to use
Other font styles liked:
• Josefins Sans Bold & Lato

Colors
f78f20
ffffff

Requirements
Must have
• - Our Logo
- Our tagline: YOUR SKIN DESERVES IT!
- Address and contact information for our locations
- Our color scheme: Black and #FAA641
- Heading font is Josefin Sans Bold
- Paragraph font is Lato
- Our website address: www.GlowDermaClinic.com

```html
<!DOCTYPE html>
<html lang="en">
<head>
<meta charset="utf-8">
<title>Glow Derma Newsletter Spread</title>
<link rel="stylesheet" href="https://fonts.googleapis.com/css2?family=Josefin+Sans:wght@600;700&family=Lato:wght@400;700&display=swap">
<style>
  :root {
    --orange: #faa641;
    --orange-deep: #f78f20;
    --ink: #1e1e1e;
    --text: #2b2b2b;
    --paper: #ffffff;
    --backdrop: #d8cec9;
    --sun-a: #f2c47a;
    --sun-b: #8c6a4a;
    --food-a: #e9583a;
    --food-b: #f2b35a;
    --spa-a: #f3ece8;
    --spa-b: #d9ccc5;
    --serum-a: #3fc0dc;
    --serum-b: #1e8fb3;
    --capsule-a: #f4efe6;
    --capsule-b: #d8c9a8;
  }
  * { box-sizing: border-box; margin: 0; padding: 0; }
  html, body { width: 1200px; height: 833px; overflow: hidden; }
  body { background: var(--backdrop); position: relative; font-family: "Lato", sans-serif; color: var(--text); }

  .spread { position: absolute; left: 20px; top: 41px; width: 1160px; height: 750px; display: flex; box-shadow: 0 10px 30px rgba(0,0,0,.18); }
  .page { position: relative; width: 580px; height: 750px; background: var(--paper); overflow: hidden; }
  .page--left { background: linear-gradient(to right, #fff 92%, #ececec 100%); }
  .page--right { background: linear-gradient(to left, #fff 92%, #ececec 100%); }

  .brand { position: absolute; top: 26px; right: 34px; display: flex; align-items: center; gap: 8px; }
  .brand__dot { width: 22px; height: 22px; border-radius: 50%; background: var(--orange-deep); }
  .brand__name { font-family: "Josefin Sans", sans-serif; font-weight: 700; font-size: 26px; color: var(--ink); }

  .heading { display: block; background: var(--orange); color: #fff; font-family: "Josefin Sans", sans-serif; font-weight: 700; font-size: 15px; height: 30px; line-height: 33px; padding-left: 22px; border-radius: 16px 0 0 16px; margin-bottom: 8px; }
  .body-text { font-size: 11.5px; line-height: 15px; }

  .tips { position: absolute; left: 28px; top: 78px; width: 270px; }
  .tip { margin-bottom: 20px; }

  .photo { position: absolute; }
  .photo--sun { left: 312px; top: 78px; width: 240px; height: 150px; background: radial-gradient(circle at 35% 45%, #fff3c9 0 8%, var(--sun-a) 22%, var(--sun-b) 100%); }
  .photo--food { left: 312px; top: 240px; width: 240px; height: 150px; background: linear-gradient(135deg, #7cb342 0%, var(--food-a) 45%, var(--food-b) 100%); }
  .photo--spa { left: 312px; top: 402px; width: 240px; height: 170px; background: linear-gradient(160deg, var(--spa-a), var(--spa-b)); }

  .footer { position: absolute; left: 0; right: 0; bottom: 26px; height: 30px; background: var(--orange); display: flex; justify-content: space-between; align-items: center; padding: 4px 26px 0; color: #fff; font-family: "Josefin Sans", sans-serif; font-weight: 700; font-size: 13px; }
  .footer__tagline { font-size: 14px; letter-spacing: .5px; }

  .article { position: absolute; left: 28px; width: 300px; }
  .article--products { top: 78px; }
  .article--claims { top: 330px; width: 330px; }
  .product-item { margin-top: 12px; position: relative; padding-right: 48px; }
  .price { position: absolute; right: 0; top: -4px; background: var(--orange); color: #fff; font-family: "Josefin Sans", sans-serif; font-weight: 700; font-size: 11px; padding: 5px 7px 3px; border-radius: 0 10px 10px 10px; }

  .photo--serum { left: 350px; top: 78px; width: 206px; height: 220px; background: linear-gradient(150deg, #eaf6f9 0 40%, var(--serum-a) 40%, var(--serum-b) 100%); }
  .photo--capsules { left: 400px; top: 330px; width: 140px; height: 160px; background: radial-gradient(ellipse at 50% 55%, var(--capsule-a), var(--capsule-b)); border-radius: 10px; }
</style>
</head>
<body>
<main class="spread">
  <section class="page page--left">
    <div class="brand"><span class="brand__dot"></span><span class="brand__name">Glow Derma</span></div>

    <div class="tips">
      <article class="tip">
        <h2 class="heading">Use Sunscreen</h2>
        <p class="body-text">Sun damage can cause premature wrinkles. Drink sufficient fluids and protect your skin with a broad-spectrum sunscreen.</p>
      </article>
      <article class="tip">
        <h2 class="heading">Eat Right</h2>
        <p class="body-text">Avoid highly processed foods and eat a balanced diet. Fresh fruits and vegetables contain antioxidants great for skin health.</p>
      </article>
      <article class="tip">
        <h2 class="heading">Stress Less</h2>
        <p class="body-text">Stress accelerates aging signs. Incorporate stress-relieving activities such as yoga and meditation to relax.</p>
      </article>
      <article class="tip">
        <h2 class="heading">Hydrate</h2>
        <p class="body-text">A lack of elasticity in dry skin means more wrinkles. Keep your skin hydrated and moisturized.</p>
      </article>
      <article class="tip">
        <h2 class="heading">Buff your Skincare Routine</h2>
        <p class="body-text">A religious skincare routine is the holy-grail to healthy skin. Incorporate skin peels and collagen to speed up cell regeneration for a more youthful tone.</p>
      </article>
    </div>

    <div class="photo photo--sun" role="img" aria-label="Silhouette of a woman against a hazy setting sun"></div>
    <div class="photo photo--food" role="img" aria-label="Platter of fresh fruit and sliced vegetables"></div>
    <div class="photo photo--spa" role="img" aria-label="Woman relaxing during a facial skin treatment"></div>

    <footer class="footer">
      <span class="footer__site">www.GlowDermaClinic.com</span>
      <span class="footer__tagline">YOUR SKIN DESERVES IT!</span>
    </footer>
  </section>

  <section class="page page--right">
    <div class="brand"><span class="brand__dot"></span><span class="brand__name">Glow Derma</span></div>

    <article class="article article--products">
      <h2 class="heading">Are There Any Effective Products?</h2>
      <p class="body-text">Although plastic surgeon, Dr. Helen Marsh, claims that no topical treatment that can be as effective as Velatox, she, amongst other doctors, advocate the below to help relax wrinkles:</p>
      <p class="body-text product-item">Peptides, specifically hexapeptides. (Recommended: Lumeva Peptide Firm Serum at)<span class="price">$275</span></p>
      <p class="body-text product-item">Collagen boosting ingredients, specifically hyaluronic acid and retinol. (Recommended: Corvelle Retinol Line Smoothing Night Serum Capsules at)<span class="price">$33</span></p>
    </article>

    <article class="article article--claims">
      <h2 class="heading">How Can I Be Aware of False Claims?</h2>
      <p class="body-text">Many innovations on the market promise the miracle of youth. Not all are FDA approved and backed with evidence. When in doubt, ask certified skincare professionals. Dr. Carla Reyes is especially skeptical of radiofrequency home devices that tout anti-aging benefits. Dr. Marsh concurs and recommends that only medical-grade skincare or prescriptions should be used. Velatox has replaced diamonds to become girls' best friend. We hope these tips will help you ride out the Velatox drought till your next appointment.</p>
    </article>

    <div class="photo photo--serum" role="img" aria-label="Blue peptide serum pump bottle"></div>
    <div class="photo photo--capsules" role="img" aria-label="Glass jar of retinol night serum capsules"></div>

    <footer class="footer">
      <span class="footer__site">www.GlowDermaClinic.com</span>
      <span class="footer__tagline">YOUR SKIN DESERVES IT!</span>
    </footer>
  </section>
</main>
</body>
</html>
```